Email Signature Block Design for Law Firm

I would like you to create a similar signature block for my law firm . I saw the email signature block attached as image002.png and wanted a similar design for my law firm. I want to be able to swap the portraits for each of my staff from the final design. Our law firm colors are black, gold, white, red.

Industry/Entity Type

Law

Requirements
Nice to have
• i like the red circle in around the photo in the 8 copper bench design. The 9 Copper Bench desgn is what inspired me to have a signature block design for my firm.

```html
<!DOCTYPE html>
<html lang="en">
<head>
<meta charset="utf-8">
<title>The Marlow Firm – Email Signature</title>
<link rel="stylesheet" href="https://fonts.googleapis.com/css2?family=Cinzel:wght@400;500;600&family=Montserrat:wght@700;800&display=swap">
<style>
  :root {
    --gold: #dc9a2a;
    --ink: #000000;
    --paper: #ffffff;
    --portrait-light: #d9d4cf;
    --portrait-dark: #2a2a2e;
  }
  * { margin: 0; padding: 0; box-sizing: border-box; }
  html, body { width: 1200px; height: 594px; overflow: hidden; background: var(--paper); }
  .signature {
    position: relative;
    width: 1200px;
    height: 594px;
    background: var(--paper);
    color: var(--ink);
    font-family: "Cinzel", serif;
  }
  .brand {
    position: absolute;
    left: 125px;
    top: 150px;
    display: flex;
    align-items: center;
    gap: 14px;
  }
  .brand-mark {
    width: 52px;
    height: 52px;
    background: var(--gold);
  }
  .brand-name {
    font-size: 22px;
    font-weight: 500;
    letter-spacing: 0.5px;
    line-height: 1;
    white-space: nowrap;
  }
  .brand-tagline {
    display: flex;
    align-items: center;
    gap: 6px;
    margin-top: 8px;
    font-family: "Montserrat", sans-serif;
    font-size: 9px;
    font-weight: 800;
    letter-spacing: 7px;
    white-space: nowrap;
  }
  .brand-tagline::before,
  .brand-tagline::after {
    content: "";
    display: block;
    width: 32px;
    height: 1px;
    background: var(--ink);
  }
  .person {
    position: absolute;
    left: 150px;
    top: 258px;
    width: 320px;
    text-align: center;
  }
  .person-name {
    font-size: 42px;
    font-weight: 500;
    line-height: 1;
    white-space: nowrap;
  }
  .person-title {
    margin-top: 8px;
    font-family: "Montserrat", sans-serif;
    font-size: 12px;
    font-weight: 800;
    letter-spacing: 6px;
  }
  .band {
    position: absolute;
    left: 85px;
    top: 392px;
    width: 1036px;
    height: 73px;
    background: var(--ink);
  }
  .website {
    position: absolute;
    left: 807px;
    top: 414px;
    color: var(--gold);
    font-size: 20px;
    font-weight: 500;
    letter-spacing: 0.3px;
  }
  .portrait-frame {
    position: absolute;
    left: 518px;
    top: 189px;
    width: 242px;
    height: 242px;
    border-radius: 50%;
    border: 12px solid var(--gold);
    background: var(--paper);
    overflow: hidden;
  }
  .portrait {
    width: 100%;
    height: 100%;
    background: radial-gradient(circle at 50% 40%, var(--portrait-light) 0%, #8c8680 35%, var(--portrait-dark) 75%);
  }
  .contacts {
    position: absolute;
    left: 860px;
    top: 264px;
    list-style: none;
  }
  .contact {
    display: flex;
    align-items: center;
    gap: 10px;
    height: 29px;
    font-size: 25px;
    font-weight: 500;
    line-height: 1;
    white-space: nowrap;
  }
  .contact-icon { width: 27px; height: 27px; flex: none; }
</style>
</head>
<body>
<main class="signature">
  <header class="brand">
    <div class="brand-mark"></div>
    <div class="brand-text">
      <div class="brand-name">The Marlow Firm, PLLC</div>
      <div class="brand-tagline">Attorneys At Law</div>
    </div>
  </header>

  <section class="person">
    <h1 class="person-name">Desmond Hale</h1>
    <p class="person-title">LOREM IMPSUM</p>
  </section>

  <div class="band"></div>
  <p class="website">HOLDTHELINELAW.COM</p>

  <figure class="portrait-frame">
    <div class="portrait" role="img" aria-label="Staff portrait: attorney in dark suit, arms crossed"></div>
  </figure>

  <ul class="contacts">
    <li class="contact">
      <svg class="contact-icon" viewBox="0 0 28 28" aria-hidden="true">
        <circle cx="14" cy="14" r="13" fill="var(--gold)"/>
        <path d="M9 7.5c1-.6 1.8-.4 2.3.5l1.2 2.3c.4.8.2 1.4-.5 1.9l-.8.6c.7 1.8 2 3.2 3.8 4l.6-.8c.5-.7 1.2-.9 1.9-.5l2.3 1.2c.9.5 1.1 1.3.5 2.3-1 1.7-2.6 2.3-4.6 1.4-3.8-1.6-6.5-4.3-8-8-.8-2 -.2-3.7 1.3-4.9z" fill="var(--paper)"/>
      </svg>
      <span>(555) 014 2870</span>
    </li>
    <li class="contact">
      <svg class="contact-icon" viewBox="0 0 28 28" aria-hidden="true">
        <rect x="2" y="5.5" width="24" height="17" rx="2" fill="none" stroke="var(--gold)" stroke-width="2"/>
        <path d="M3 7l11 8.5L25 7" fill="none" stroke="var(--gold)" stroke-width="2"/>
      </svg>
      <span>LOREM IPSUM</span>
    </li>
    <li class="contact">
      <svg class="contact-icon" viewBox="0 0 28 28" aria-hidden="true">
        <circle cx="14" cy="14" r="11.5" fill="none" stroke="var(--gold)" stroke-width="2.2"/>
      </svg>
      <span>LOREM IPSUM</span>
    </li>
  </ul>
</main>
</body>
</html>
```